Vorla Pty Ltd business card design

We need a business card for our company who is involved in upper market residential property development.
Design should be elegant and contemporary.

Our residences are inspired and elegant in contemporary design, combined with inviting ambience. We produce exclusive boutique developments which appeal to the most discerning of purchasers.
We would like to see a design to reflect the above.

Industry/Entity Type

Residential

Contact Information for Business Card

Vorla Pty Ltd, Marek Dunsworth, PO Box 58 Kelvale 3194 Melbourne AUSTRALIA, ph (+61 3) 0427 5926 84

Logo Text

Vorla Pty Ltd

```html
<!DOCTYPE html>
<html lang="en">
<head>
<meta charset="utf-8">
<title>Vorla Pty Ltd – Business Card</title>
<link rel="stylesheet" href="https://fonts.googleapis.com/css2?family=Open+Sans:wght@400;600;700&display=swap">
<style>
  :root {
    --plum: #93247f;
    --plum-faint: #e9d6e6;
    --taupe: #aea69c;
    --ink: #1a1a1a;
    --paper: #ffffff;
    --stage: #2a2a2a;
    --stage-edge: #141414;
  }
  * { box-sizing: border-box; margin: 0; padding: 0; }
  html, body { width: 1200px; height: 1200px; overflow: hidden; }
  body {
    background: radial-gradient(circle at 50% 45%, var(--stage) 0%, var(--stage-edge) 100%);
    font-family: "Open Sans", Arial, sans-serif;
    position: relative;
  }
  .card {
    position: absolute;
    left: 167px;
    width: 866px;
    height: 520px;
    border-radius: 30px;
    overflow: hidden;
  }
  .card--back { top: 45px; background: var(--plum); }
  .card--front { top: 635px; background: var(--paper); }

  .back-mark {
    position: absolute;
    left: 80px; top: 190px;
    width: 300px; height: 300px;
    border: 14px solid rgba(255,255,255,0.22);
    border-radius: 26px;
  }

  .card-bands { position: absolute; inset: 0; width: 100%; height: 100%; }

  .front-mark {
    position: absolute;
    left: 560px; top: 150px;
    width: 250px; height: 200px;
    border: 12px solid var(--plum-faint);
    border-radius: 22px;
  }

  .brand { position: absolute; left: 150px; top: 130px; }
  .brand-square {
    position: absolute; left: 0; top: 30px;
    width: 70px; height: 70px;
    background: var(--plum);
  }
  .brand-name {
    position: absolute; left: 100px; top: 0;
    font-size: 84px; font-weight: 600; line-height: 1;
    color: var(--plum); white-space: nowrap;
  }
  .brand-tag {
    position: absolute; left: 104px; top: 100px;
    background: var(--taupe); color: var(--paper);
    font-size: 17px; font-weight: 400; letter-spacing: 6px;
    padding: 4px 12px; white-space: nowrap;
  }

  .person { position: absolute; left: 480px; top: 70px; }
  .person-name { font-size: 32px; font-weight: 600; color: var(--plum); white-space: nowrap; }
  .person-company { font-size: 21px; font-weight: 600; color: var(--ink); margin-top: 2px; }

  .contact {
    position: absolute; left: 150px; top: 315px;
    font-size: 25px; font-weight: 600; color: var(--ink); line-height: 1.3;
  }
  .contact-phone { margin-top: 14px; }
</style>
</head>
<body>
  <section class="card card--back" aria-label="Card back">
    <div class="back-mark"></div>
  </section>

  <section class="card card--front" aria-label="Card front">
    <div class="front-mark"></div>
    <svg class="card-bands" viewBox="0 0 866 520" aria-hidden="true">
      <path d="M0 455 H532 L545 382 H866 V392 H554 L541 465 H0 Z" fill="var(--taupe)"/>
      <path d="M0 478 H548 L562 402 H866 V520 H0 Z" fill="var(--plum)"/>
      <path d="M760 402 L866 300 V402 Z" fill="var(--plum)"/>
    </svg>

    <div class="brand">
      <div class="brand-square"></div>
      <div class="brand-name">Vorla</div>
      <div class="brand-tag">Vorla Pty Ltd.</div>
    </div>

    <div class="person">
      <div class="person-name">Marek Dunsworth</div>
      <div class="person-company">Vorla Pty Ltd,</div>
    </div>

    <div class="contact">
      <p>PO Box 58 Kelvale 3194</p>
      <p>Melbourne AUSTRALIA,</p>
      <p class="contact-phone">ph (+61 3) 0427 5926 84</p>
    </div>
  </section>
</body>
</html>
```